Business card design needed for a security services business.

We provide a wide range of security services from guard personnel to electronic systems.

Industry/Entity Type

Security Industry

Contact Information for Business Card

Brent Holloway, Owner Office: 780.555.0148; Cell: 780.555.0193 Email: brent@korvanshieldgroup.example; Address 20417 163 St Edmonton, AB T5X 2K8

Colors
0054AA
0677BA
7BADD7
CADEEF
E8F1F8

Requirements
Nice to have
• On the back of the card I would like to possible list the services I provide: Guards Mobiles Live Video Surveillance Access Intrusion

```html
<!DOCTYPE html>
<html lang="en">
<head>
<meta charset="UTF-8">
<title>Korvan Shield Group – Business Card</title>
<link href="https://fonts.googleapis.com/css2?family=Poppins:wght@400;600;700&display=swap" rel="stylesheet">
<style>
  :root {
    --brand-blue: #0a6cc2;
    --text-grey: #666666;
    --text-dark: #222222;
    --card-white: #ffffff;
    --backdrop: #e6e6e6;
    --card-edge: #3a3a3a;
  }
  html, body {
    margin: 0;
    padding: 0;
    width: 1200px;
    height: 900px;
    overflow: hidden;
    background: var(--backdrop);
    font-family: "Poppins", sans-serif;
  }
  .canvas {
    position: relative;
    width: 1200px;
    height: 900px;
  }
  .card {
    position: absolute;
    top: 217px;
    width: 308px;
    height: 499px;
    background: var(--card-white);
    box-shadow: 2px 2px 0 var(--card-edge);
  }
  .card--back {
    left: 279px;
    border-radius: 0 66px 0 66px;
  }
  .card--front {
    left: 617px;
    border-radius: 66px 0 66px 0;
  }
  .wordmark {
    position: absolute;
    left: 0;
    width: 100%;
    text-align: center;
    color: var(--brand-blue);
    font-weight: 700;
    font-size: 22px;
    line-height: 1.15;
    letter-spacing: 0.5px;
    text-transform: uppercase;
  }
  .card--back .wordmark { top: 140px; }
  .card--front .wordmark { top: 118px; }
  .services {
    position: absolute;
    left: 49px;
    top: 340px;
    margin: 0;
    padding: 0;
    list-style: none;
    font-size: 14px;
    line-height: 18px;
    letter-spacing: 0.2px;
  }
  .services li:nth-child(odd) { color: var(--brand-blue); }
  .services li:nth-child(even) { color: var(--text-grey); }
  .person {
    position: absolute;
    left: 32px;
    top: 284px;
  }
  .person__name {
    margin: 0;
    color: var(--brand-blue);
    font-weight: 700;
    font-size: 22px;
    line-height: 24px;
    letter-spacing: -0.3px;
    text-transform: uppercase;
  }
  .person__title {
    margin: 0;
    color: var(--text-dark);
    font-size: 14px;
    line-height: 16px;
    text-transform: uppercase;
  }
  .contact {
    position: absolute;
    left: 32px;
    top: 340px;
    margin: 0;
    padding: 0;
    list-style: none;
    font-size: 14px;
    line-height: 17px;
    color: var(--text-dark);
  }
  .contact li {
    display: flex;
    align-items: center;
    gap: 5px;
    margin-bottom: 1px;
  }
  .contact svg {
    width: 13px;
    height: 13px;
    flex: none;
    fill: var(--brand-blue);
  }
  .address {
    position: absolute;
    left: 35px;
    top: 413px;
    margin: 0;
    font-style: normal;
    font-size: 14px;
    line-height: 18px;
    color: var(--text-dark);
  }
</style>
</head>
<body>
<main class="canvas">
  <section class="card card--back" aria-label="Card back">
    <div class="wordmark">Korvan Shield<br>Group</div>
    <ul class="services">
      <li>GUARDS</li>
      <li>MOBILES LIVE</li>
      <li>VIDEO SURVEILLANCE</li>
      <li>ACCESS INTRUSION</li>
    </ul>
  </section>

  <section class="card card--front" aria-label="Card front">
    <div class="wordmark">Korvan Shield<br>Group</div>
    <div class="person">
      <p class="person__name">Brent Holloway</p>
      <p class="person__title">Owner</p>
    </div>
    <ul class="contact">
      <li>
        <svg viewBox="0 0 24 24" aria-hidden="true"><path d="M6.6 10.8a15.1 15.1 0 0 0 6.6 6.6l2.2-2.2a1 1 0 0 1 1-.25 11.4 11.4 0 0 0 3.6.57 1 1 0 0 1 1 1V20a1 1 0 0 1-1 1A17 17 0 0 1 3 4a1 1 0 0 1 1-1h3.5a1 1 0 0 1 1 1c0 1.25.2 2.45.57 3.57a1 1 0 0 1-.25 1z"/></svg>
        <span>780.555.0148</span>
      </li>
      <li>
        <svg viewBox="0 0 24 24" aria-hidden="true"><path d="M6.6 10.8a15.1 15.1 0 0 0 6.6 6.6l2.2-2.2a1 1 0 0 1 1-.25 11.4 11.4 0 0 0 3.6.57 1 1 0 0 1 1 1V20a1 1 0 0 1-1 1A17 17 0 0 1 3 4a1 1 0 0 1 1-1h3.5a1 1 0 0 1 1 1c0 1.25.2 2.45.57 3.57a1 1 0 0 1-.25 1z"/></svg>
        <span>780.555.0193</span>
      </li>
      <li>
        <svg viewBox="0 0 24 24" aria-hidden="true"><path d="M2 5h20v14H2z M2 5l10 8 10-8" fill="var(--brand-blue)"/><path d="M2 5l10 8 10-8" fill="none" stroke="#fff" stroke-width="1.6"/></svg>
        <span>brent@korvanshieldgroup.example</span>
      </li>
    </ul>
    <address class="address">20417 163 St Edmonton<br>AB T5X 2K8</address>
  </section>
</main>
</body>
</html>
```